Lottery Scratchcard templates for charities

We produce scratch cards for charities to sell to their supporters to raise funds.

We need a set of templates which can be re-used for different clients by simply replacing text, logo, prizes and a potentially a picture.

One of the templates can be plain simply using block colours
One can use generic images like a treasure chests which indicate money can be won
One templates can feature space for a photograph which can be easily replaced and updated depending on the client - example, a picture of a dog for a dog charity can easily be replaced by a picture of a football team for a club.

Target Market(s)

People who support a charity and the charities themselves

Industry/Entity Type

Charity

Colors

Designer to choose colors to be used in the design.

Requirements
Must have
• Every card will need space for:
• - The charity's logo
• - our logo
• - a panel which can be scratched off (use a plain silver, but can have an image printed on top in black only)
• - information about how to win (this can be lorem ipsum text)
• - Prizes (usually 4 or 5 prize levels of £100, £50, £10, £1)
• - Price: £1 and/or Just £1 to play
• - Small print - "Please play responsibly www.KeelbrookTrust.org."
• minimum size 4pt
• Paper size: A7, print ready
• Format: Adobe InDesign, fully editable
• Vector illustrations/design elements

```html
<!DOCTYPE html>
<html lang="en">
<head>
<meta charset="utf-8">
<title>Support the Community – £1 Scratchcard</title>
<link rel="stylesheet" href="https://fonts.googleapis.com/css2?family=Montserrat:wght@400;500;800;900&display=swap">
<style>
  :root {
    --page: #ffffff;
    --gold-light: #ffe66b;
    --gold: #fbc21d;
    --orange: #f39a12;
    --orange-deep: #e8850c;
    --red: #e31d25;
    --white: #ffffff;
    --cream: #fff6dc;
    --ink: #111111;
    --silver-top: #ececec;
    --silver-mid: #d9d9d9;
    --silver-low: #c9c9c9;
    --serial-mark: #a9a9a9;
  }
  * { box-sizing: border-box; margin: 0; padding: 0; }
  html, body { width: 1200px; height: 1200px; overflow: hidden; background: var(--page); }
  body { position: relative; font-family: "Montserrat", Arial, sans-serif; }

  .scratchcard {
    position: absolute; left: 288px; top: 130px; width: 646px; height: 928px;
    overflow: hidden;
    background:
      radial-gradient(circle at 52% 42%, #fffbe0 0%, var(--gold-light) 18%, var(--gold) 45%, var(--orange) 80%, var(--orange-deep) 100%);
  }

  .brand-tab {
    position: absolute; left: 142px; top: 0; width: 365px; height: 133px;
    background: var(--white); border-radius: 0 0 62px 62px;
    display: flex; align-items: center; justify-content: center;
  }
  .brand-tab__name {
    font-weight: 900; font-size: 40px; letter-spacing: 1px; color: var(--red);
    margin-top: -2px;
  }

  .price-badge {
    position: absolute; left: 527px; top: 24px; width: 86px; height: 86px;
    border-radius: 50%; background: var(--white);
    display: flex; align-items: center; justify-content: center;
    font-weight: 900; font-size: 36px; color: var(--ink);
  }

  .headline { position: absolute; left: 0; top: 220px; width: 646px; height: 150px; }
  .headline text {
    font-family: "Montserrat", Arial, sans-serif; font-weight: 900;
    fill: var(--cream); stroke: var(--red); paint-order: stroke fill;
    stroke-linejoin: round; text-anchor: middle;
  }

  .treasure-art {
    position: absolute; left: 192px; top: 350px; width: 380px; height: 170px;
    border-radius: 40px 60px 10px 10px;
    background: radial-gradient(ellipse at 40% 45%, #fff3a0 0%, #f2bd2a 35%, #b77a2c 75%, #8a5a24 100%);
  }

  .charity-tab {
    position: absolute; left: 232px; top: 466px; width: 182px; height: 56px;
    background: var(--red); border-radius: 22px 22px 0 0;
    display: flex; justify-content: center; padding-top: 16px;
    color: var(--white); font-weight: 800; font-size: 11px;
  }

  .scratch-panel {
    position: absolute; left: 77px; top: 517px; width: 493px; height: 305px;
    border: 5px solid var(--red); border-radius: 14px; overflow: hidden;
    background: linear-gradient(176deg, var(--silver-top) 0%, var(--silver-mid) 52%, var(--silver-low) 52.3%, var(--silver-mid) 100%);
  }
  .prize {
    position: absolute; width: 150px; text-align: center; color: var(--ink);
  }
  .prize__amount { display: block; font-weight: 900; font-size: 38px; line-height: 40px; letter-spacing: -0.5px; }
  .prize__amount small { font-size: 28px; }
  .prize__word { display: block; font-weight: 500; font-size: 14px; line-height: 16px; }

  .serial {
    position: absolute; right: 54px; bottom: 9px; font-size: 13px; color: var(--ink);
  }
  .serial mark { background: var(--serial-mark); color: var(--ink); padding: 2px 3px; }

  .small-print {
    position: absolute; left: 78px; top: 850px; width: 493px;
    font-size: 8.4px; line-height: 11.4px; color: var(--white); text-align: justify;
  }
</style>
</head>
<body>
  <article class="scratchcard">
    <header class="brand-tab"><span class="brand-tab__name">LOGO</span></header>
    <div class="price-badge">£1</div>

    <svg class="headline" viewBox="0 0 646 150" aria-label="Support the Community">
      <text x="306" y="56" font-size="44" stroke-width="8">SUPPORT THE</text>
      <text x="323" y="135" font-size="92" stroke-width="9">COMMUNITY</text>
    </svg>

    <div class="treasure-art" role="img" aria-label="Open treasure chest overflowing with gold coins"></div>

    <div class="charity-tab">KeelbrookTrust.org</div>

    <section class="scratch-panel" aria-label="Scratch panel">
      <div class="prize" style="left:25px;top:48px"><span class="prize__amount">£10.<small>00</small></span><span class="prize__word">TEN</span></div>
      <div class="prize" style="left:182px;top:48px"><span class="prize__amount">£100</span><span class="prize__word">HUNDRED</span></div>
      <div class="prize" style="left:328px;top:48px"><span class="prize__amount">£1.<small>00</small></span><span class="prize__word">ONE</span></div>

      <div class="prize" style="left:25px;top:124px"><span class="prize__amount">£10.<small>00</small></span><span class="prize__word">TEN</span></div>
      <div class="prize" style="left:175px;top:124px"><span class="prize__amount">£50</span><span class="prize__word">FIFTY</span></div>
      <div class="prize" style="left:325px;top:124px"><span class="prize__amount">£1.<small>00</small></span><span class="prize__word">ONE</span></div>

      <div class="prize" style="left:21px;top:200px"><span class="prize__amount">£1.<small>00</small></span><span class="prize__word">ONE</span></div>
      <div class="prize" style="left:178px;top:200px"><span class="prize__amount">£100</span><span class="prize__word">HUNDRED</span></div>
      <div class="prize" style="left:316px;top:200px"><span class="prize__amount">£50</span><span class="prize__word">FIFTY</span></div>

      <p class="serial">0567 3456 21 56634 32111 <mark>23344 55</mark></p>
    </section>

    <p class="small-print">Scratch off the silver panel to reveal nine prize amounts. Match three identical amounts to win that prize. Claim prizes from the seller within 30 days. Players must be 16 or over. Please play responsibly www.KeelbrookTrust.org. Proceeds support local community projects and services run by the charity.</p>
  </article>
</body>
</html>
```